Wedding Company needs Brochure Design

FOR THIS PROJECT, WE ARE LOOKING FOR A BROCHURE. WHOEVER WE CHOOSE AS THE WINNING BROCHURE DESIGN WILL THEN DESIGN OUR WEBSITE AND BUSINESS CARD.

We're are looking to expand our brochure by making it a circle and adding 6 inside pages of information with a front and back cover. The pages will be as follows:

Front
About us
About us pictures
Wedding Planning
Wedding planning pictures
Lighting & Decor
Lighting & decor pictures
Back

We've uploaded a picture of our current brochure... so you can get an idea of what we've liked before. Please give us your creative input & design ideas. We've put together a "mock" brochure for you to take a look at as well. As you can see we need your help to properly lay out pictures so that the pages look full and the pictures pop and catches our clients attention.

A few words to describe our brochure would be "elegance", "class", "tasteful" and "colorful". We want to be able to portray that we are luxurious and innovative for the higher end brides and at the same time catering to the budget friendly brides.

Currently, we are waiting on a few pictures from the photographers and we are hoping to have them in a few days... In the meantime we've placed pictures we took from our phone as place holders.

Industry/Entity Type

Catering

```html
<!DOCTYPE html>
<html lang="en">
<head>
<meta charset="utf-8">
<title>Wedding Planning &amp; Co-ordination – Brochure Spread</title>
<link rel="stylesheet" href="https://fonts.googleapis.com/css2?family=Handlee&family=Dancing+Script:wght@700&display=swap">
<style>
  :root {
    --backdrop: #3d4245;
    --ring-light: #e4e4e4;
    --ring-mid: #c4c4c4;
    --ring-dark: #a9a9a9;
    --paper: #dcdcdc;
    --paper-edge: #d2d2d2;
    --white: #ffffff;
    --ink: #5f6468;
    --ink-dark: #3e4245;
  }
  * { margin: 0; padding: 0; box-sizing: border-box; }
  html, body {
    width: 1200px;
    height: 583px;
    overflow: hidden;
    background: var(--backdrop);
  }
  .spread {
    position: relative;
    width: 1200px;
    height: 583px;
  }
  .spread-art {
    position: absolute;
    inset: 0;
  }
  .page-copy {
    position: absolute;
    left: 142px;
    top: 130px;
    width: 400px;
    color: var(--ink-dark);
  }
  .page-title {
    font-family: "Handlee", cursive;
    font-weight: 400;
    font-size: 31px;
    line-height: 34px;
    color: var(--ink);
    text-align: center;
    margin-bottom: 26px;
  }
  .page-intro,
  .service-lead,
  .service-list {
    font-family: "Dancing Script", cursive;
    font-weight: 700;
    font-size: 11.5px;
    line-height: 15px;
  }
  .page-intro {
    text-align: center;
    margin-bottom: 14px;
  }
  .service-lead {
    padding-left: 56px;
    margin-bottom: 10px;
  }
  .service-list {
    padding-left: 56px;
    width: 330px;
  }
</style>
</head>
<body>
<main class="spread">
  <svg class="spread-art" width="1200" height="583" viewBox="0 0 1200 583" xmlns="http://www.w3.org/2000/svg">
    <defs>
      <radialGradient id="ring-finish" cx="45%" cy="40%" r="65%">
        <stop offset="0%" stop-color="var(--ring-light)"/>
        <stop offset="70%" stop-color="var(--ring-mid)"/>
        <stop offset="100%" stop-color="var(--ring-dark)"/>
      </radialGradient>
      <clipPath id="photo-disc">
        <circle cx="871" cy="292" r="236"/>
      </clipPath>
    </defs>

    <!-- Left page: text disc -->
    <g class="text-page">
      <circle cx="342" cy="292" r="265" fill="url(#ring-finish)"/>
      <circle cx="342" cy="292" r="252" fill="none" stroke="var(--white)" stroke-width="1.5" stroke-dasharray="4 4"/>
      <circle cx="342" cy="292" r="240" fill="var(--white)"/>
      <circle cx="342" cy="292" r="234" fill="var(--paper)" stroke="var(--paper-edge)" stroke-width="1"/>
    </g>

    <!-- Right page: photo disc -->
    <g class="photo-page">
      <circle cx="871" cy="292" r="265" fill="url(#ring-finish)"/>
      <circle cx="871" cy="292" r="252" fill="none" stroke="var(--white)" stroke-width="1.5" stroke-dasharray="4 4"/>
      <circle cx="871" cy="292" r="240" fill="var(--white)"/>
      <g clip-path="url(#photo-disc)">
        <rect x="630" y="50" width="480" height="117" fill="#3a3550" role="img" aria-label="Photo of wedding guests celebrating on the dance floor"/>
        <rect x="630" y="173" width="161" height="360" fill="#9a5fa8" role="img" aria-label="Photo of a purple and pink floral arrangement"/>
        <rect x="799" y="173" width="187" height="211" fill="#d8b9a6" role="img" aria-label="Photo of a reception hall with white ceiling drapes and uplighting"/>
        <rect x="993" y="173" width="110" height="211" fill="#8c8a9c" role="img" aria-label="Photo of a couple embracing outdoors at sunset"/>
        <rect x="799" y="392" width="187" height="140" fill="#4f5a3c" role="img" aria-label="Photo of two grooms walking down a garden aisle"/>
        <rect x="993" y="392" width="110" height="140" fill="#6d6a6c" role="img" aria-label="Photo of a couple at the ceremony with guests"/>
      </g>
    </g>
  </svg>

  <section class="page-copy">
    <h1 class="page-title">Wedding Planning &amp;<br>Co-ordination</h1>
    <p class="page-intro">With all the success and joy we have experienced in providing our expertise and quality services we are now prepared to include the planning and execution of your entire wedding. We've partnered together with top notch vendors in the Southern California area to put together a phenomenal wedding full of unforgettable memories for both the happy couple and their guests. We are your one stop shop for all things weddings!</p>
    <p class="service-lead">We can assist you in finding the following:<br>- Caterer - Bartending Services</p>
    <p class="service-list">-Florist - Cake - Photographer - Rentals Linens - DJ or Band Services - Dress Stores - Planning and Coordination</p>
  </section>
</main>
</body>
</html>
```